New Infusion Pharmacy needs Business Card design

Hello!

We are Meridale Infusion Pharmacy, are we are looking for a two sided, clean and modern business card.

First, let me give you a little bit about what an infusion pharmacy does...
We compound and fill prescriptions for drugs that are injectable, meaning that they are administered via an IV bag or a syringe. Basically anything that is too advanced for a normal pill pharmacy to fill. We compound everything in our state of the art clean room, then deliver it directly to the patients home. We have an outside sales force that markets to hospitals, home health agencies, and doctor's offices.

as for the business card...
We are looking for a clean, modern card. our colors are in our logo, kind of a light bule and a darker blue. We do really like the rounded corners on the card. Also, we would like the back of the card to be the reverse colors of the front, for example, if the front of the card has a light background, then the back of the card will have a dark background.

On the back side of the card we want to have our logo, then list some of the services we offer:
-IVIG
-TPN
-Enteral Nutrition
-IV Antibiotics
-IV Hydration
-Blood Factors
-Chemotherapy
-Pain Management

Our logo is uploaded in .psd format, if you need a different format let me know and i'll throw it up here.

Thank you so much!!

Industry/Entity Type

Pharmacy

Requirements
Must have
• Front of Card: (no particular order, please arrange in whatever way you think looks best!)
-Employee Name
-Title
-Office Phone #
-Cell Phone #
-Fax #
-email address - tobin@meridaleinfusion-example.com
-office address - 4127 Harlow St. Ashvale, CA 90000
-Web Site - www.meridaleinfusion-example.com

```html
<!DOCTYPE html>
<html lang="en">
<head>
<meta charset="utf-8">
<title>Meridale Infusion Pharmacy – Business Card</title>
<link rel="stylesheet" href="https://fonts.googleapis.com/css2?family=Ubuntu:wght@400;500;700&display=swap">
<style>
  :root {
    --bg: #e6e8ea;
    --card-light: #ffffff;
    --card-blue: #1597bf;
    --brand-dark: #0d4f6b;
    --brand-light: #1a9cc4;
    --ink-white: #ffffff;
  }
  * { box-sizing: border-box; margin: 0; padding: 0; }
  html, body {
    width: 1200px; height: 900px; overflow: hidden;
    background: var(--bg);
    font-family: "Ubuntu", sans-serif;
  }
  .stage { position: relative; width: 1200px; height: 900px; }

  .card {
    position: absolute;
    left: 290px;
    width: 620px; height: 355px;
    border-radius: 26px;
    overflow: hidden;
    box-shadow: 0 10px 28px rgba(0,0,0,.18);
  }

  /* Services side */
  .card--services { top: 60px; background: var(--card-light); }
  .brand-block {
    position: absolute; left: 70px; top: 62px;
    color: var(--brand-dark); font-weight: 500;
  }
  .brand-block .brand-name { font-size: 76px; letter-spacing: 1px; line-height: 1; }
  .brand-block .brand-sub { font-size: 22px; letter-spacing: 9px; margin-top: 8px; }
  .divider {
    position: absolute; left: 0; right: 0; top: 218px;
    height: 2px; background: var(--brand-dark);
  }
  .services {
    position: absolute; left: 0; right: 0; top: 236px;
    text-align: center; color: var(--brand-dark);
    font-size: 18px; line-height: 1.35; font-weight: 400;
  }

  /* Contact side */
  .card--contact { top: 485px; background: var(--card-blue); }
  .brand-vertical {
    position: absolute; left: 30px; top: 338px;
    transform: rotate(-90deg); transform-origin: left top;
    color: var(--brand-dark); font-weight: 500; white-space: nowrap;
  }
  .brand-vertical .brand-name { font-size: 64px; line-height: 1; letter-spacing: 1px; }
  .brand-vertical .brand-sub { font-size: 17px; letter-spacing: 7px; margin-top: 4px; }

  .contact { position: absolute; left: 220px; top: 52px; color: var(--ink-white); }
  .person .name { font-size: 26px; font-weight: 400; letter-spacing: .5px; }
  .person .title { font-size: 16px; }
  .person .title::before { content: "| "; }
  .lines { list-style: none; margin-top: 28px; font-size: 17px; line-height: 1.3; }
  .lines b { display: inline-block; width: 26px; font-weight: 700; }
  .address { margin-top: 24px; font-size: 17px; }
  .web { margin-top: 18px; font-size: 17px; font-weight: 700; }
</style>
</head>
<body>
<main class="stage">
  <section class="card card--services" aria-label="Card back with services">
    <div class="brand-block">
      <div class="brand-name">MERIDALE</div>
      <div class="brand-sub">INFUSION PHARMACY</div>
    </div>
    <div class="divider"></div>
    <p class="services">
      IVIG • TPN • Enteral Nutrition • IV Antibiotics<br>
      IV Hydration • Blood Factors • Chemotherapy<br>
      Pain Management
    </p>
  </section>

  <section class="card card--contact" aria-label="Card front with contact details">
    <div class="brand-vertical">
      <div class="brand-name">MERIDALE</div>
      <div class="brand-sub">INFUSION PHARMACY</div>
    </div>
    <div class="contact">
      <p class="person"><span class="name">TOBIN MARSH</span> <span class="title">Operation Manager</span></p>
      <ul class="lines">
        <li><b>T</b>(555) 01 482 30 16</li>
        <li><b>M</b>(555) 01 947 52 88</li>
        <li><b>F</b>(555) 01 482 30 16</li>
        <li><b>E</b>tobin@meridaleinfusion-example.com</li>
      </ul>
      <p class="address">4127 Harlow St. Ashvale, CA 90000</p>
      <p class="web">www.meridaleinfusion-example.com</p>
    </div>
  </section>
</main>
</body>
</html>
```